Stationery Design Project

We need letterhead and business cards designed for our consulting firm. Color scheme, mostly deep blue (see logo). We are a commercial consulting work out firm, nationwide (large loans, $10MM and up). Visit our website for more info.
Updates

Project Deadline Extended
Reason: Meeting tomorrow morning to make final final decision. Would like this project to stay open to be able to provide feed back and receive final edits and approve. Thank you!!!

Target Market(s)

High end investors

Industry/Entity Type

Business

Requirements
Must have
• Letterhead must have the logo and the address

4817 Larkmoor Avenue, Suite 210, San Diego, CA 92107
Nice to have
• It would be nice to incorporate a watermark of all or some portion of the logo on the letterhead, or at least for the 2nd sheets.

Maybe our phone number: 858.555.0174
and/or webiste: www.tollandridgecap.example
Should not have
• Target users and audience of this will be men so, frilly or whimsical type designs are not preferred.

```html
<!DOCTYPE html>
<html lang="en">
<head>
<meta charset="utf-8">
<title>Tolland Ridge Capital — Stationery</title>
<link rel="stylesheet" href="https://fonts.googleapis.com/css2?family=Cinzel:wght@400&family=Arimo:wght@400&display=swap">
<style>
  :root {
    --board-light: #f4f4f4;
    --board-dark: #8a8a8a;
    --ink: #111111;
    --card-black: #050505;
    --brand-grey: #8d929b;
    --brand-grey-light: #c4c8ce;
    --card-blue: #3fb0ee;
    --card-blue-pale: #d4eefb;
    --paper: #fbfbfb;
    --paper-edge: #7d7d7d;
  }
  * { box-sizing: border-box; margin: 0; padding: 0; }
  html, body { width: 777px; height: 1200px; overflow: hidden; }
  body { font-family: "Arimo", Arial, sans-serif; color: var(--ink); }

  .board {
    position: relative;
    width: 777px; height: 1200px;
    background: linear-gradient(215deg, var(--board-light) 0%, #d2d2d2 35%, var(--board-dark) 100%);
    border: 1px solid #6f6f6f;
  }

  .brand-name {
    font-family: "Cinzel", "Trajan Pro", serif;
    font-weight: 400;
    color: var(--brand-grey);
    line-height: 1.05;
    text-align: center;
    white-space: nowrap;
  }

  .hero-mark { position: absolute; left: 52px; top: 160px; width: 300px; font-size: 34px; }

  .section-label {
    position: absolute;
    font-size: 16px;
    letter-spacing: 0.2px;
    color: var(--ink);
  }
  .label-card { left: 483px; top: 62px; }
  .label-letterhead { left: 91px; top: 338px; }

  .card { position: absolute; border-radius: 14px; }
  .card-front {
    left: 484px; top: 87px; width: 247px; height: 141px;
    background: var(--card-black);
    z-index: 2;
  }
  .card-front .brand-name {
    position: absolute; left: 92px; top: 62px; width: 144px;
    font-size: 14px; color: var(--brand-grey-light);
  }
  .card-back {
    left: 400px; top: 210px; width: 246px; height: 142px;
    background: var(--card-blue);
    border: 1px solid #2a7fb0;
    z-index: 1;
  }
  .card-details {
    position: absolute; left: 58px; top: 44px;
    list-style: none;
    font-size: 9.5px; line-height: 11.5px; color: #101820;
  }
  .card-details li { position: relative; padding-left: 14px; }
  .card-details li::before {
    content: ""; position: absolute; left: 0; top: 2px;
    width: 2px; height: 6px; background: var(--ink);
  }
  .card-details .name { font-size: 11px; line-height: 12px; }
  .card-details .tagline { font-size: 5px; line-height: 6px; padding-left: 28px; }
  .card-details .tagline::before { display: none; }
  .card-details .indent { padding-left: 57px; }
  .card-details .indent::before { display: none; }

  .letterhead {
    position: absolute; left: 87px; top: 368px; width: 599px; height: 777px;
    background: var(--paper);
    border: 1px solid var(--paper-edge);
  }
  .letterhead-tab {
    position: absolute; left: -1px; top: -1px; width: 160px; height: 92px;
    background: var(--card-black);
    border-radius: 0 0 12px 0;
    border-top-left-radius: 6px;
  }
  .letterhead-tab .brand-name {
    position: absolute; left: 10px; top: 30px; width: 140px;
    font-size: 14px; color: var(--brand-grey-light);
  }
  .letterhead-watermark {
    position: absolute; left: 148px; top: 360px; width: 304px;
    font-size: 32px; color: #dde0e4;
  }
  .letterhead-footer {
    position: absolute; left: 190px; top: 726px; width: 409px; height: 51px;
    background: linear-gradient(90deg, var(--card-blue) 0%, #7ccbf3 55%, var(--card-blue-pale) 100%);
    border: 1px solid #5a6e7a;
    border-radius: 8px 0 8px 8px;
  }
  .footer-details {
    position: absolute; left: 28px; top: 3px;
    list-style: none;
    font-size: 9.5px; line-height: 11px; color: #101820;
  }
  .footer-square {
    position: absolute; right: 12px; top: 14px;
    width: 22px; height: 22px; background: var(--brand-grey);
  }
</style>
</head>
<body>
<main class="board">
  <div class="brand-name hero-mark">Tolland Ridge<br>Capital</div>

  <h2 class="section-label label-card">BUSINESS CARD</h2>

  <section class="card card-front" aria-label="Business card front">
    <div class="brand-name">Tolland Ridge<br>Capital</div>
  </section>

  <section class="card card-back" aria-label="Business card back">
    <ul class="card-details">
      <li class="name">TOLLAND RIDGE</li>
      <li class="tagline">CAPITAL</li>
      <li>Address : 4817 Larkmoor Avenue,</li>
      <li class="indent">Suite 210,</li>
      <li>&nbsp;<span style="padding-left:43px">San Diego,</span></li>
      <li class="indent">CA 92107</li>
      <li>phone number: 858.555.0174</li>
      <li>Email: info@tollandridgecap.example</li>
      <li>webiste: www.tollandridgecap.example</li>
    </ul>
  </section>

  <h2 class="section-label label-letterhead">LETTER HEAD</h2>

  <section class="letterhead" aria-label="Letterhead">
    <div class="letterhead-tab">
      <div class="brand-name">Tolland Ridge<br>Capital</div>
    </div>
    <div class="brand-name letterhead-watermark" aria-hidden="true">Tolland Ridge<br>Capital</div>
    <footer class="letterhead-footer">
      <ul class="footer-details">
        <li>Address : 4817 Larkmoor Avenue,Suite 210,San Diego,CA 92107</li>
        <li>phone number: 858.555.0174</li>
        <li>Email: info@tollandridgecap.example</li>
        <li>webiste: www.tollandridgecap.example</li>
      </ul>
      <span class="footer-square" aria-hidden="true"></span>
    </footer>
  </section>
</main>
</body>
</html>
```